Bref créative
Brisk Lattice Cards & Stationary
Project #2
Corporate
Carl Wendimeer
VP of Business Development
2841 Thornbury Lane
Linden Falls, MN 55612
cwendimeer@brisklattice-mail.com
www.brisklattice-mail.com
Here is our logo

```html
<!DOCTYPE html>
<html lang="en">
<head>
<meta charset="utf-8">
<title>Brisk Lattice Stationery</title>
<link rel="stylesheet" href="https://fonts.googleapis.com/css2?family=Open+Sans:wght@400;600;700&display=swap">
<style>
  :root {
    --page: #ffffff;
    --frame: #e3e3e3;
    --paper: #ffffff;
    --edge: #d6d6d6;
    --brand: #1f6fb5;
    --ink: #6b6b6b;
    --flap: #c9c9c9;
  }
  * { box-sizing: border-box; margin: 0; padding: 0; }
  html, body { width: 1200px; height: 681px; overflow: hidden; background: var(--page); }
  body { font-family: "Open Sans", sans-serif; color: var(--ink); position: relative; }

  .showcase-frame {
    position: absolute; left: 19px; top: 19px; width: 1162px; height: 641px;
    border: 2px solid var(--frame); border-radius: 4px;
  }
  .sheet { position: absolute; background: var(--paper); border: 1px solid var(--edge); }

  .brand-mark { display: flex; align-items: center; gap: 8px; }
  .brand-mark__square { background: var(--brand); flex: none; }
  .brand-mark__name {
    font-weight: 700; color: var(--brand); text-transform: uppercase;
    letter-spacing: 0.02em; line-height: 1;
  }

  /* Envelope front */
  .envelope-front { left: 62px; top: 96px; width: 351px; height: 204px; }
  .envelope-front .brand-mark { position: absolute; left: 14px; top: 10px; }
  .envelope-front .brand-mark__square { width: 34px; height: 34px; }
  .envelope-front .brand-mark__name { font-size: 17px; }
  .envelope-front__return { position: absolute; left: 14px; top: 58px; font-size: 6.5px; }

  /* Envelope back */
  .envelope-back { left: 62px; top: 343px; width: 351px; height: 204px; }
  .envelope-back__flap { position: absolute; inset: 0; }
  .envelope-back .brand-mark {
    position: absolute; left: 50%; top: 88px; transform: translateX(-50%);
  }
  .envelope-back .brand-mark__square { width: 14px; height: 14px; }
  .envelope-back .brand-mark__name { font-size: 10px; }

  /* Letterhead */
  .letterhead { left: 619px; top: 43px; width: 307px; height: 576px; }
  .letterhead .brand-mark { position: absolute; left: 14px; top: 18px; }
  .letterhead .brand-mark__square { width: 38px; height: 38px; }
  .letterhead .brand-mark__name { font-size: 18px; }
  .letterhead__contact {
    position: absolute; left: 14px; top: 78px; font-size: 6.5px; line-height: 1.55;
  }

  /* Business card */
  .business-card { left: 967px; top: 182px; width: 185px; height: 108px; }
  .business-card .brand-mark { position: absolute; left: 8px; top: 8px; gap: 5px; }
  .business-card .brand-mark__square { width: 16px; height: 16px; }
  .business-card .brand-mark__name { font-size: 9px; }
  .business-card__details {
    position: absolute; left: 8px; top: 50px; font-size: 4.6px; line-height: 1.55;
  }
  .business-card__person {
    position: absolute; left: 100px; top: 50px; font-size: 4.6px; line-height: 1.55;
  }
  .business-card__name { font-weight: 700; color: var(--brand); }
</style>
</head>
<body>
  <div class="showcase-frame"></div>

  <section class="sheet envelope-front" aria-label="Envelope front">
    <div class="brand-mark">
      <span class="brand-mark__square"></span>
      <span class="brand-mark__name">Brisk Lattice</span>
    </div>
    <p class="envelope-front__return">2841 Thornbury Lane, Linden Falls, MN 55612</p>
  </section>

  <section class="sheet envelope-back" aria-label="Envelope back">
    <svg class="envelope-back__flap" width="351" height="204" viewBox="0 0 351 204">
      <path d="M2 2 L12 14 Q175 90 339 14 L349 2" fill="none" stroke="var(--flap)" stroke-width="1"/>
    </svg>
    <div class="brand-mark">
      <span class="brand-mark__square"></span>
      <span class="brand-mark__name">Brisk Lattice</span>
    </div>
  </section>

  <section class="sheet letterhead" aria-label="Letterhead">
    <div class="brand-mark">
      <span class="brand-mark__square"></span>
      <span class="brand-mark__name">Brisk Lattice</span>
    </div>
    <address class="letterhead__contact" style="font-style:normal">
      2841 Thornbury Lane<br>
      Linden Falls, MN 55612<br>
      Phone 952.555.0147<br>
      cwendimeer@brisklattice-mail.com<br>
      www.brisklattice-mail.com
    </address>
  </section>

  <section class="sheet business-card" aria-label="Business card">
    <div class="brand-mark">
      <span class="brand-mark__square"></span>
      <span class="brand-mark__name">Brisk Lattice</span>
    </div>
    <address class="business-card__details" style="font-style:normal">
      2841 Thornbury Lane<br>
      Linden Falls, MN 55612<br>
      Phone 952.555.0147<br>
      Mobile 952.555.0193<br>
      cwendimeer@brisklattice-mail.com
    </address>
    <div class="business-card__person">
      <p class="business-card__name">Carl Wendimeer</p>
      <p>VP of Business Development</p>
    </div>
  </section>
</body>
</html>
```